Tavner Golf Academy Brochure Design Project

We need a tri- fold brochure for our golf academy. Tavner Golf Academy was founded by Dale Tavner, a strength coach on the NLK Circuit. Our Academy fuses Swing instruction, 3D biomechanic analysis and fitness training. We would like to incorporate the colors green, grey/silver and possible black. The final design should communicate movement/action and health.
Updates
The brochure is tri fold, double sided. Front cover should include logo, and a photo of a golfer. inside should include a a history of our company, and the services we offer(I will provide). Back middle panel should be white, with logo on the top and space for address and contact info on the bottom (we currently have 2 locations, and may want to tailor this information). The other fold in should include testamonials (I will provide). Thank you.
Include the following Titles, pictures and descriptions under 'Service'
Industry/Entity Type
Fitness
Requirements
Must have
- photos of people recieving golf instruction, people performing functional exercise training (stability balls, tubing, medicine balls, stretching) We would like to designate a space to give a description of each of our services: 1)Golf Performance Evaluation. 2)Swing Coaching. 3)3D and Video Feedback Coaching. 4)Golf Performance (fitness) Coaching.
Testimonials from the Pros:
“I have trained exclusively with Dale for the last several years. Under his guidance, I have greatly enhanced my power, flexibility, and endurance on the course. As Head Strength and Conditioning Coach for the NLK, Dale personalizes cutting-edge golf fitness programs for me, so I know that every day I play, I am at the top of my game. As Dale’s fitness student and friend, I will thoroughly enjoy watching him create one of the world’s foremost golf performance companies.” - Tod Bramwell, 16 time NLK Circuit winner, Winner of the 2003 Corvane Classic, 2010 Halvery Trophy Champion
“Dale has really helped me take my golf fitness to the next level. Preventing injury, strength training, stability, flexibility, and generating power are some of the areas we have worked on and improved!” - Matías Orduna, 3 time NLK Circuit winner, 3 time Westmarch State College All American, 2 time MVC Player of the Year
“Dale Tavner is one of the most knowledgeable and enthusiastic trainers in the business. Whether it be golf specific, bust your butt or light stretching, Dale has a varied, experienced and fun way to train!”- Glen Purdey, Winner, 2005 Morton Quill Award, 8 time NLK Circuit winner, 20 professional wins
“I trust and rely on Dale to get me ready for every round of golf that I play on the NLK Circuit. He is definitely one of the best in the industry.”- Wendell Pruitt, NLK Circuit Professional Golfer, Winner, 2007 Lyle Dunmore Vantrex Invitational, 2010 Ostrava Mutual Championship
“Since I started working with Dale my endurance, flexibility and strength have improved dramatically. His golf specific program has really shored up the weak areas of my body. He has also really helped me come back from my knee and back injuries.” - Lonnie Gressett, 4 time NLK Circuit Winner

```html
<!DOCTYPE html>
<html lang="en">
<head>
<meta charset="utf-8">
<title>Tavner Golf Academy – Tri-fold Brochure</title>
<link href="https://fonts.googleapis.com/css2?family=Arimo:wght@400;700&family=Marcellus&family=Open+Sans:ital,wght@0,600;1,400&display=swap" rel="stylesheet">
<style>
  :root{
    --forest:#104c2a;
    --green:#1b8a3e;
    --bright:#22a04a;
    --grey:#8f8f91;
    --photo:#6e7f78;
    --white:#ffffff;
    --black:#000000;
    --ink:#1d1d1d;
  }
  *{margin:0;padding:0;box-sizing:border-box}
  html,body{width:806px;height:1200px;overflow:hidden;background:var(--white)}
  body{position:relative;font-family:"Arimo",Arial,sans-serif}
  .panel{position:absolute}
  .strip{position:absolute;background:var(--forest)}
  .grey{background:var(--grey)}

  /* outside spread */
  .info{left:34px;top:0;width:234px;height:570px;padding:34px 7px 0 19px;color:var(--white);font-size:9.1px;line-height:11.2px;letter-spacing:-.15px;text-align:justify}
  .info h3{color:var(--forest);font-weight:400;font-size:9.1px;margin-bottom:1px}
  .info p + h3{margin-top:22px}
  .info p + p{margin-top:11px}

  .back{left:268px;top:0;width:269px;height:570px}
  .back-band{position:absolute;left:14px;top:0;width:255px;height:48px;background:linear-gradient(#e6e6e6,#a9a9ab);border-radius:0 0 4px 4px;display:flex;align-items:center;justify-content:center}
  .back-band span{font-family:"Open Sans",sans-serif;font-weight:600;font-size:12px;color:var(--forest)}
  .location{position:absolute;left:0;width:269px;text-align:center;font-family:"Open Sans",sans-serif;font-weight:600;font-size:9.4px;line-height:11.4px;color:var(--green)}
  .location strong{color:var(--ink);font-weight:600}

  .cover{left:537px;top:0;width:269px;height:570px}
  .brand{position:absolute;left:4px;top:8px;height:48px;display:flex;align-items:center;gap:8px}
  .brand i{width:40px;height:40px;border-radius:50%;background:var(--bright);display:block}
  .brand span{font-family:"Open Sans",sans-serif;font-weight:600;font-size:19px;color:var(--bright)}
  .cover-photo{position:absolute;left:0;top:63px;width:269px;height:507px;background:var(--photo)}

  /* inside spread */
  .history{left:34px;top:629px;width:234px;height:571px;padding:22px 7px 0 20px;color:var(--white);font-size:9.1px;line-height:11.3px;letter-spacing:-.15px;text-align:justify}
  .heading{font-family:"Marcellus",serif;color:var(--green);font-size:17px;text-align:center;font-weight:400;letter-spacing:.3px}
  .history .heading{margin-bottom:20px;margin-left:-12px}
  .history p + p{margin-top:12px}

  .services{left:268px;top:629px;width:269px;height:571px}
  .services .heading{position:absolute;left:0;top:20px;width:206px}
  .service-box{position:absolute;background:var(--black)}
  .photo{position:absolute}
  .service-title{font-weight:700;font-size:8.8px;line-height:10.5px;letter-spacing:-.2px;white-space:nowrap}
  .service-text{font-size:7.6px;line-height:9.4px;letter-spacing:-.15px}
  .swing-text{position:absolute;left:130px;top:5px;width:120px;color:var(--white)}
  .bio-text{position:absolute;left:6px;top:253px;width:90px;color:var(--ink)}
  .perf-text{position:absolute;left:134px;top:409px;width:128px;color:var(--ink)}

  .testimonials{left:537px;top:629px;width:235px;height:571px;padding:19px 6px 0 9px;overflow:hidden}
  .testimonials .heading{margin-bottom:11px}
  .quote{font-family:"Open Sans",sans-serif;font-style:italic;font-size:7.5px;line-height:9.9px;color:var(--ink);overflow:hidden}
  .quote + .quote{margin-top:13px}
  .portrait{width:62px;height:74px;border:2px solid var(--white);margin:2px 8px 2px 0}
  .quote.right .portrait{float:right;margin:6px 0 2px 6px}
  .quote.left .portrait{float:left}
</style>
</head>
<body>

<!-- Outside: info panel -->
<div class="strip" style="left:0;top:0;width:34px;height:570px"></div>
<section class="panel info grey">
  <h3>Driving Range</h3>
  <p>Get warmed up at our driving range, fully equipped with 60 bays (20 heated) and yard markers up to 300 yards. You'll love practicing with our AutoTee® system, automatically teeing up your ball with every shot you make. AutoTee enables you to choose from four separate tee heights and provides a platform for timing and muscle memory that is unrivaled. We offer bucket sizes ranging from 60-140 balls, as well as discount packs for customers who wish to pre-pay.</p>
  <h3>Golf Instructions</h3>
  <p>Learn from the best with golf lessons taught by NLK™ Teaching Professionals. At Tavner Golf Academy, with our seasoned instructors, you can work on every aspect of your game in our outdoor bays, on our par-3 golf course or indoors using one of our netted bays. Our instructors will work on every aspect of your swing to learning proper golf etiquette. Enroll in one of our golf schools/semi-private lessons, and you'll learn the basics of playing golf, or opt for our private lessons which are available in half-hour and one-hour sessions. Be sure to ask about our indoor golf instruction lessons and packages</p>
  <h3>Parties &amp; Special Events</h3>
  <p>Plan your birthday party with us, allowing your friends and family to participate in any of our golf course facilities, including miniature golf.</p>
  <p>***Reserve a picnic area for your guests, with catering and refreshments provided upon request. Our facility also makes a unique destination for school events and corporate parties.</p>
</section>

<!-- Outside: back panel -->
<section class="panel back">
  <div class="back-band"><span>Tavner Golf Academy</span></div>
  <div class="location" style="top:386px">
    <strong>Tavner Golf Academy</strong><br>48 Linden Court<br>Marlow Falls, NJ 10000<br>XXX.XXX.XXXX<br>www.tavnergolfacademy.com
  </div>
  <div class="location" style="top:459px">
    <strong>Tavner Golf Academy</strong><br>610 County Road 4<br>Marlow Falls, NJ 10002-4100<br>555.204.0171<br>www.tavnergolfacademy.com
  </div>
</section>

<!-- Outside: cover -->
<section class="panel cover">
  <div class="brand"><i></i><span>Tavner Golf Academy</span></div>
  <div class="cover-photo" role="img" aria-label="Photo of a golfer finishing his swing on a misty course at sunrise"></div>
</section>

<!-- Inside: history -->
<div class="strip" style="left:0;top:629px;width:34px;height:571px"></div>
<section class="panel history grey">
  <h2 class="heading">Our History</h2>
  <p>How and where the history of golf originated is for the most part is unknown and continues to be the subject of much debate. Although, for the most part it is widely understood that the Scots during the middle ages where largely responsible for creating the game of golf we play today, a claim that has undergone substantial scrutiny and numerous challenges over many centuries.</p>
  <p>There are several forerunners to the history of golf dating back as far as early 1297 to the Netherlands, leaving the Dutch to appear to have the closest ties to the origin of golf. Further evidence is supported by early 13th Century Dutch literature which contained numerous references to "golf like" games with medieval names such as "spel mitten colve" (play with club). Additionally, Dutch master painters of the day created numerous paintings and sketches of early participants playing a game with a club and ball in Holland, most certainly resembling what we know today as golf.</p>
  <p>Commerce between Scotland and Holland blossomed throughout the North Sea trade route during the beginning of the middle ages. Sailors and traders often became stranded or delayed due to bad weather and became perfect candidates to become introduced to a new and better way to enjoy their leisure time and began to participate in the favorite local sports of the day. In many instances, some of the players shown in Dutch pictures were kilts giving a clear indication they were Scottish visitors.</p>
</section>

<!-- Inside: services -->
<section class="panel services">
  <h2 class="heading">Services</h2>

  <div class="service-box" style="left:8px;top:52px;width:252px;height:170px">
    <svg class="photo" style="left:9px;top:5px" width="99" height="124" role="img" aria-label="Photo of a golfer in a blue shirt at the top of his backswing outdoors">
      <rect width="99" height="124" fill="#6a8f4e"/><rect width="99" height="58" fill="#8fb0d6"/>
    </svg>
    <svg class="photo" style="left:125px;top:55px" width="110" height="109" role="img" aria-label="Photo of an instructor coaching a student's swing on a practice range">
      <rect width="110" height="109" fill="#557d3f"/><rect width="110" height="40" fill="#9aa89a"/>
    </svg>
    <div class="swing-text">
      <div class="service-title">SWING COACHING:</div>
      <div class="service-text">Swing Coaching focuses on teaching the fundamentals of the golf swing from the set-up, grip, aim, alignment, and club path</div>
    </div>
  </div>

  <div class="service-box" style="left:100px;top:253px;width:160px;height:118px">
    <svg class="photo" style="left:0;top:0" width="160" height="118" role="img" aria-label="Screen of 3D biomechanics swing analysis beside a golfer wearing motion sensors">
      <rect width="160" height="118" fill="#111"/><rect x="14" y="10" width="48" height="96" fill="#2c4a22"/><rect x="70" y="8" width="84" height="102" fill="#e4e8e4"/>
    </svg>
  </div>
  <div class="bio-text">
    <div class="service-title">3D BIOMECHANICS:</div>
    <div class="service-text">Our 3D Biomechanics training focuses on developing an efficient golf swing via the kinematic sequence. Effortless power and a safe, efficient and reproducible swing are developed</div>
  </div>

  <svg class="photo" style="left:18px;top:409px" width="106" height="129" role="img" aria-label="Photo of athletes doing stability ball and tubing exercises in a bright studio">
    <rect width="106" height="129" fill="#d9d2c2"/><rect y="80" width="106" height="49" fill="#b59a6a"/>
  </svg>
  <div class="perf-text">
    <div class="service-title">PERFORMANCE TRAINING:</div>
    <div class="service-text">Performance Training focuses on improving specific mobility, stability and core strength that allow golfer's to feel and play their best. Other exercises strategies are also employed to produce efficient, powerful and durable golfers</div>
  </div>
</section>

<!-- Inside: testimonials -->
<section class="panel testimonials grey">
  <h2 class="heading">Testimonials</h2>

  <div class="quote left">
    <svg class="portrait" role="img" aria-label="Photo of Tod Bramwell after a swing"><rect width="100%" height="100%" fill="#4d6b3c"/></svg>
    “I have trained exclusively with Dale for the last several years. Under his guidance, I have greatly enhanced my power, flexibility, and endurance on the course. As Head Strength and Conditioning Coach for the NLK, Dale personalizes cutting-edge golf fitness programs for me, so I know that every day I play, I am at the top of my game. As Dale's fitness student and friend, I will thoroughly enjoy watching him create one of the world's foremost golf performance companies.” - Tod Bramwell, 16 time NLK Circuit winner, Winner of the 2003 Corvane Classic, 2010 Halvery Trophy Champion
  </div>

  <div class="quote right">
    <svg class="portrait" style="width:70px;height:54px" role="img" aria-label="Photo of Matías Orduna crouched reading a putt"><rect width="100%" height="100%" fill="#5e7a44"/></svg>
    “Dale has really helped me take my golf fitness to the next level. Preventing injury, strength training, stability, flexibility, and generating power are some of the areas we have worked on and improved!” - Matías Orduna, 3 time NLK Circuit winner, 3 time Westmarch State College All American, 2 time MVC Player of the Year
  </div>

  <div class="quote left">
    <svg class="portrait" style="height:64px" role="img" aria-label="Photo of Glen Purdey on the course"><rect width="100%" height="100%" fill="#52734a"/></svg>
    “Dale Tavner is one of the most knowledgeable and enthusiastic trainers in the business. Whether it be golf specific, bust your butt or light stretching, Dale has a varied, experienced and fun way to train!” - Glen Purdey, Winner, 2005 Morton Quill Award, 8 time NLK Circuit winner and 20 professional wins.
  </div>

  <div class="quote right">
    <svg class="portrait" style="width:56px;height:66px" role="img" aria-label="Photo of Wendell Pruitt holding a trophy"><rect width="100%" height="100%" fill="#4f6f8a"/></svg>
    “I trust and rely on Dale to get me ready for every round of golf that I play on the NLK Circuit. He is definitely one of the best in the industry.” - Wendell Pruitt, NLK Circuit Professional Golfer, Winner, 2007 Lyle Dunmore Vantrex Invitational, 2010 Ostrava Mutual Championship
  </div>

  <div class="quote left">
    <svg class="portrait" style="height:64px" role="img" aria-label="Photo of Lonnie Gressett smiling on the course"><rect width="100%" height="100%" fill="#5a7a48"/></svg>
    “Since I started working with Dale my endurance, flexibility and strength have improved dramatically. His golf specific program has really shored up the weak areas of my body. He has also really helped me come back from my knee and back injuries.” - Lonnie Gressett, 4 time NLK Circuit Winner
  </div>
</section>
<div class="strip" style="left:772px;top:629px;width:34px;height:571px"></div>

</body>
</html>
```